Thermostat Screen Design

We need a screen layout design for a new thermostat we're currently developing. If you're not familiar with thermostats, you can see some examples here - http://heating-dials-compared.bestlistguide.example/

We're after the main page design, with icons, colours etc. It needs to be clean, modern and minimalistic. Attached is all components required on the screen. The screen size is 5 inch (diagnol).

The arrows on the screen showcase what happens when you press a button. For example, when you press MODE once you get OFF, press it twice, HEAT, press it 3 times, COOL, etc. This is just for your reference.

You have complete creative license on how you choose to layout the screen, position the components etc, but we require:

- it must be on a 5 inch screen diagnol
- modern, clean and minimalistic
- includes icons and colours
- Intuitive

Let me know if any questions.

```html
<!DOCTYPE html>
<html lang="en">
<head>
<meta charset="utf-8">
<title>Thermostat Screen Design</title>
<link rel="stylesheet" href="https://fonts.googleapis.com/css2?family=Open+Sans:wght@400;600;700&display=swap">
<style>
:root{
  --page:#c6c9f6;
  --screen:#0e2f63;
  --screen-deep:#0b2a58;
  --topbar:#101820;
  --panel:#1d4272;
  --panel-line:#3a5f8d;
  --nav:#3d5a82;
  --nav-active:#9cc3f2;
  --nav-line:#5a7aa3;
  --icon:#8fb8ec;
  --white:#ffffff;
  --heat:#ff3b3b;
  --cool:#8cc4ff;
  --caption:#5d6079;
  --control:#6f8dba;
}
*{margin:0;padding:0;box-sizing:border-box}
html,body{width:800px;height:1200px;overflow:hidden}
body{background:var(--page);font-family:'Open Sans',Arial,sans-serif;position:relative}

.screen{position:absolute;left:160px;top:54px;width:480px;height:272px;background:var(--screen);overflow:hidden}
.topbar{height:26px;background:var(--topbar);color:var(--white);font-size:13px;letter-spacing:2px;text-align:center;line-height:26px}
.zone{position:absolute;left:190px;top:30px;width:90px;text-align:center;color:var(--white);font-size:13px;font-weight:600;letter-spacing:2px}
.room-temp{position:absolute;left:40px;top:28px;color:var(--white);font-weight:700;font-size:118px;line-height:1;letter-spacing:-3px}
.room-temp .deg{position:absolute;left:138px;top:18px;font-size:30px;font-weight:400}
.room-temp .unit{position:absolute;left:164px;top:54px;font-size:60px;font-weight:400;letter-spacing:0}
.reading{position:absolute;top:146px;color:var(--white);text-align:center}
.reading .value{font-size:40px;font-weight:700;line-height:1;letter-spacing:-1px}
.reading .value sup{font-size:14px;font-weight:400;vertical-align:top;position:relative;top:4px}
.reading .value small{font-size:18px;font-weight:400}
.reading .label{font-size:11px;margin-top:2px}
.reading.outdoor{left:36px}
.reading.indoor{left:150px}
.setpoint{position:absolute;left:248px;width:80px;text-align:center}
.setpoint .value{font-size:30px;font-weight:700;line-height:1}
.setpoint .value sup{font-size:11px;vertical-align:top}
.setpoint .label{font-size:7px;color:var(--white);letter-spacing:.3px;white-space:nowrap}
.setpoint.heat{top:50px}
.setpoint.heat .value{color:var(--heat)}
.setpoint.cool{top:112px}
.setpoint.cool .value{color:var(--cool)}
.adjust{position:absolute;left:332px;top:58px;width:124px;height:128px;background:var(--panel);border:1px solid var(--panel-line)}
.adjust .half{height:50%;border-bottom:1px solid var(--panel-line);display:flex;align-items:center;justify-content:center;color:#7b98c0;font-size:40px;font-weight:300}
.adjust .half:last-child{border-bottom:none}
.gauge{position:absolute;left:460px;top:58px;width:7px;height:128px;background:linear-gradient(#ff2f4a,#ffc23a 35%,#8be84a 65%,#2ee6e0)}
.nav{position:absolute;left:0;bottom:0;width:100%;height:52px;display:flex;background:var(--nav);border-top:1px solid var(--nav-line)}
.nav .tab{flex:1;display:flex;align-items:center;justify-content:center;border-left:1px solid var(--nav-line);color:var(--icon);font-size:30px;font-weight:700}
.nav .tab:first-child{border-left:none}
.nav .tab.active{background:var(--nav-active);color:#4f7fc0}

.zoom{position:absolute;border-radius:50%;overflow:hidden;background:var(--screen-deep)}
.zoom-icons{left:44px;top:420px;width:320px;height:320px}
.zoom-icons .cool-value{position:absolute;left:52px;top:-28px;color:var(--cool);font-size:66px;font-weight:700;line-height:1}
.zoom-icons .cool-value sup{font-size:20px;vertical-align:top}
.zoom-icons .cool-label{position:absolute;left:40px;top:62px;color:var(--white);font-size:15px;font-weight:600}
.zoom-icons .panel{position:absolute;left:190px;top:6px;width:160px;height:140px;background:var(--panel);border:2px solid var(--panel-line)}
.zoom-icons .panel::after{content:"";position:absolute;left:88px;top:80px;width:30px;height:4px;background:#6b88b3}
.zoom-icons .navbar{position:absolute;left:0;top:208px;width:100%;height:112px;background:var(--nav);border-top:2px solid var(--nav-line)}
.zoom-icons .divider{position:absolute;left:242px;top:0;width:2px;height:100%;background:var(--nav-line)}
.zoom-icons .gear{position:absolute;left:92px;top:26px}

.zoom-gauge{left:404px;top:814px;width:312px;height:312px}
.zoom-gauge .panel{position:absolute;left:38px;top:30px;width:166px;height:250px;background:var(--panel);border:2px solid var(--panel-line)}
.zoom-gauge .half{height:50%;border-bottom:2px solid var(--panel-line);position:relative}
.zoom-gauge .half:last-child{border-bottom:none}
.zoom-gauge .bar{position:absolute;background:var(--control)}
.zoom-gauge .gauge-bar{position:absolute;left:214px;top:20px;width:14px;height:262px;background:linear-gradient(#ff2f4a,#ffc23a 35%,#8be84a 65%,#2ee6e0)}

.caption{position:absolute;color:var(--caption);font-size:40px;font-weight:600;letter-spacing:15px;line-height:50px}
.caption.icons{left:434px;top:500px}
.caption.gauge-caption{left:64px;top:918px}
</style>
</head>
<body>

<section class="screen" aria-label="Thermostat main screen">
  <div class="topbar">10:30 AM</div>
  <div class="zone">ZONE 2</div>
  <div class="room-temp">72<span class="deg">o</span><span class="unit">F</span></div>
  <div class="reading outdoor"><div class="value">90<sup>o</sup><small>F</small></div><div class="label">Outdoor Temp.</div></div>
  <div class="reading indoor"><div class="value">40<sup>%</sup></div><div class="label">Indoor Hum.</div></div>
  <div class="setpoint heat"><div class="value">89<sup>o</sup></div><div class="label">HEAT SET POINT</div></div>
  <div class="setpoint cool"><div class="value">60<sup>o</sup></div><div class="label">COOL SET POINT</div></div>
  <div class="adjust"><div class="half">+</div><div class="half">–</div></div>
  <div class="gauge"></div>
  <nav class="nav">
    <div class="tab active">
      <svg width="22" height="18" viewBox="0 0 22 18"><g fill="#4f7fc0"><rect y="0" width="22" height="3"/><rect y="7" width="22" height="3"/><rect y="14" width="22" height="3"/></g></svg>
    </div>
    <div class="tab">
      <svg width="34" height="34" viewBox="0 0 34 34"><circle cx="17" cy="17" r="15" fill="none" stroke="var(--icon)" stroke-width="3"/><g fill="var(--icon)"><path d="M17 17 C12 14 11 8 16 6 C21 6 21 12 17 17Z"/><path d="M17 17 C22 15 27 18 26 23 C23 27 18 23 17 17Z"/><path d="M17 17 C17 22 12 27 8 24 C6 19 12 17 17 17Z"/></g><circle cx="17" cy="17" r="2.5" fill="var(--nav)"/></svg>
    </div>
    <div class="tab">
      <svg width="30" height="30" viewBox="0 0 30 30"><g fill="var(--icon)"><circle cx="15" cy="15" r="10"/><rect x="12" y="1" width="6" height="28"/><rect x="1" y="12" width="28" height="6"/><rect x="12" y="1" width="6" height="28" transform="rotate(45 15 15)"/><rect x="12" y="1" width="6" height="28" transform="rotate(-45 15 15)"/></g><circle cx="15" cy="15" r="4.5" fill="var(--nav)"/></svg>
    </div>
    <div class="tab">Z</div>
  </nav>
</section>

<div class="zoom zoom-icons" aria-label="Close-up of the icon bar">
  <div class="cool-value">60<sup>o</sup></div>
  <div class="cool-label">COOL SET POINT</div>
  <div class="panel"></div>
  <div class="navbar">
    <div class="divider"></div>
    <svg class="gear" width="56" height="56" viewBox="0 0 30 30"><g fill="var(--icon)"><circle cx="15" cy="15" r="10"/><rect x="12" y="1" width="6" height="28"/><rect x="1" y="12" width="28" height="6"/><rect x="12" y="1" width="6" height="28" transform="rotate(45 15 15)"/><rect x="12" y="1" width="6" height="28" transform="rotate(-45 15 15)"/></g><circle cx="15" cy="15" r="4.5" fill="var(--nav)"/></svg>
  </div>
</div>
<div class="caption icons">SIMPLE<br>CLEAN<br>ICONS</div>

<div class="caption gauge-caption">TEMP.<br>U/I GAUGE</div>
<div class="zoom zoom-gauge" aria-label="Close-up of the temperature controls and gauge">
  <div class="panel">
    <div class="half"><span class="bar" style="left:4px;top:57px;width:74px;height:11px"></span><span class="bar" style="left:35px;top:25px;width:11px;height:75px"></span></div>
    <div class="half"><span class="bar" style="left:14px;top:60px;width:40px;height:8px"></span></div>
  </div>
  <div class="gauge-bar"></div>
</div>

</body>
</html>
```